Business Card

We need a business card designed using one of the attached logo designs (our preference is for the boxes version, but if you think it looks better with the horizontal version we will consider those too). Standard business card dimensions.

Details that need to be included:

Tobias Freel
Morlanex S.L.U
tobias@morlanex.example

Phone numbers:
(UK) +44 771 4052 368
(Spain) +34 681 503 427

Twitter: @Morlanex
Web: http://www.morlanex.example

Tagline (optional, if it doesnt make it look too cluttered):
Automation and configuration management specialists
or
Configuration management specialists

```html
<!DOCTYPE html>
<html lang="en">
<head>
<meta charset="utf-8">
<title>Morlanex Business Card</title>
<link rel="stylesheet" href="https://fonts.googleapis.com/css2?family=Questrial&family=Quicksand:wght@500;600;700&display=swap">
<style>
  :root {
    --page-bg: #1e1e1f;
    --card-top: #d2d3d5;
    --card-bottom: #f4f4f5;
    --brand-blue: #2aa6df;
    --mark-blue: #4aaee3;
    --ink: #1d1d1d;
    --ink-strong: #2a2a2a;
    --rule: #2b2b2b;
  }
  * { box-sizing: border-box; margin: 0; padding: 0; }
  html, body {
    width: 1200px;
    height: 1000px;
    overflow: hidden;
    background: var(--page-bg);
  }
  .card {
    position: absolute;
    left: 237px;
    top: 261px;
    width: 726px;
    height: 478px;
    background: linear-gradient(to bottom, var(--card-top), var(--card-bottom));
    transform: scale(1.4);
    transform-origin: center center;
    color: var(--ink);
  }
  .brand {
    position: absolute;
    left: 60px;
    top: 124px;
    width: 202px;
    text-align: center;
  }
  .brand-square {
    display: block;
    width: 182px;
    height: 180px;
    margin: 0 auto;
    background: var(--mark-blue);
  }
  .brand-name {
    display: block;
    margin-top: 10px;
    font-family: "Quicksand", sans-serif;
    font-weight: 700;
    font-size: 33px;
    letter-spacing: 1px;
    color: var(--ink-strong);
    line-height: 1;
  }
  .divider {
    position: absolute;
    left: 279px;
    top: 83px;
    width: 3px;
    height: 300px;
    background: var(--rule);
  }
  .identity {
    position: absolute;
    left: 390px;
    top: 88px;
    font-family: "Questrial", sans-serif;
  }
  .person-name {
    font-size: 32px;
    line-height: 36px;
    color: var(--brand-blue);
    text-transform: uppercase;
  }
  .company-name {
    font-size: 30px;
    line-height: 38px;
    color: var(--ink);
  }
  .contacts {
    position: absolute;
    left: 304px;
    top: 208px;
    font-family: "Quicksand", sans-serif;
    color: var(--ink);
  }
  .contact-row {
    display: flex;
    align-items: baseline;
  }
  .contact-label {
    width: 82px;
    font-weight: 700;
    font-size: 18px;
  }
  .contact-value {
    font-weight: 600;
    font-size: 19px;
  }
  .contact-value.email {
    font-family: "Questrial", sans-serif;
    font-weight: 400;
    font-size: 25px;
    line-height: 30px;
  }
  .phone-lines { line-height: 27px; }
  .row-email { height: 34px; }
  .row-phone { height: 56px; }
  .row-twitter, .row-web { height: 28px; }
  .tagline {
    position: absolute;
    left: 0;
    width: 726px;
    top: 412px;
    text-align: center;
    font-family: "Quicksand", sans-serif;
    font-weight: 600;
    font-size: 24px;
    color: var(--brand-blue);
  }
</style>
</head>
<body>
  <div class="card">
    <div class="brand">
      <span class="brand-square"></span>
      <span class="brand-name">MORLANEX</span>
    </div>

    <div class="divider"></div>

    <div class="identity">
      <p class="person-name">Tobias Freel</p>
      <p class="company-name">Morlanex S.L.U</p>
    </div>

    <div class="contacts">
      <div class="contact-row row-email">
        <span class="contact-label">e-mail:</span>
        <span class="contact-value email">tobias@morlanex.example</span>
      </div>
      <div class="contact-row row-phone">
        <span class="contact-label">phone:</span>
        <span class="contact-value phone-lines">(UK) +44 771 4052 368<br>(Spain) +34 681 503 427</span>
      </div>
      <div class="contact-row row-twitter">
        <span class="contact-label">twitter:</span>
        <span class="contact-value">@Morlanex</span>
      </div>
      <div class="contact-row row-web">
        <span class="contact-label">web:</span>
        <span class="contact-value">http://www.morlanex.example</span>
      </div>
    </div>

    <p class="tagline">Configuration management specialists</p>
  </div>
</body>
</html>
```